BKT Consulting

Government/Entitlement Consulting Services- I assist developers obtain entitlements from local, state and federal government agencies so that they can build their projects. Often these projects are very complicated and political and may face community opposition.

Target Market(s)

Real Estate Developers

Industry/Entity Type

Business Consultant

Contact Information for Business Card

Dana Velmonte
Principal

Font styles to use
Serif
Sans Serif

Requirements
Must have
• Classy and professional appeal.
Nice to have
• I like a combination of a mat and glossy finish. I've seen that done with black and then a bold color for a pop, but am not 100% committed to that.

```html
<!DOCTYPE html>
<html lang="en">
<head>
<meta charset="utf-8">
<title>BKT Consulting – Business Card</title>
<link href="https://fonts.googleapis.com/css2?family=Montserrat:wght@600&family=Source+Sans+3:wght@400;600&display=swap" rel="stylesheet">
<style>
  :root {
    --navy: #0c1452;
    --grey: #7a7a7a;
    --white: #ffffff;
    --backdrop: #e9e7e4;
    --text-light: #f2f3f8;
  }
  * { margin: 0; padding: 0; box-sizing: border-box; }
  html, body {
    width: 1200px;
    height: 900px;
    overflow: hidden;
    background: var(--backdrop);
  }
  .canvas {
    position: relative;
    width: 1200px;
    height: 900px;
  }
  .card {
    position: absolute;
    width: 556px;
    height: 343px;
    overflow: hidden;
    box-shadow: 0 6px 18px rgba(0, 0, 0, 0.18);
  }

  /* Front card */
  .card-front {
    left: 238px;
    top: 62px;
    background: var(--navy);
    color: var(--text-light);
    font-family: "Source Sans 3", "Segoe UI", sans-serif;
  }
  .identity {
    position: absolute;
    left: 46px;
    top: 62px;
  }
  .identity .name {
    font-size: 19px;
    font-weight: 600;
    line-height: 1.1;
  }
  .identity .role {
    font-size: 15px;
    font-weight: 400;
    line-height: 1.3;
  }
  .address {
    position: absolute;
    left: 46px;
    top: 164px;
    font-size: 14.5px;
    line-height: 20px;
    font-style: normal;
  }
  .contact-list {
    position: absolute;
    left: 46px;
    top: 219px;
    list-style: none;
    font-size: 14.5px;
    line-height: 20px;
  }
  .contact-list li {
    display: flex;
    align-items: center;
    gap: 8px;
  }
  .contact-list svg {
    width: 12px;
    height: 12px;
    fill: var(--text-light);
    flex: none;
  }
  .brand-band {
    position: absolute;
    right: 0;
    top: 0;
    width: 96px;
    height: 100%;
    background: var(--grey);
    display: flex;
    align-items: center;
    justify-content: center;
  }
  .brand-band .brand-name {
    writing-mode: vertical-rl;
    transform: rotate(180deg);
    font-family: "Montserrat", "Arial", sans-serif;
    font-weight: 600;
    font-size: 34px;
    letter-spacing: 1px;
    color: var(--white);
    text-transform: uppercase;
    white-space: nowrap;
  }

  /* Back card */
  .card-back {
    left: 457px;
    top: 518px;
    width: 560px;
    background: var(--white);
    display: flex;
    align-items: center;
    justify-content: center;
  }
  .card-back .brand-name {
    font-family: "Montserrat", "Arial", sans-serif;
    font-weight: 600;
    font-size: 40px;
    letter-spacing: 1px;
    color: var(--navy);
    text-transform: uppercase;
    margin-top: 6px;
  }
</style>
</head>
<body>
<main class="canvas">

  <section class="card card-front" aria-label="Business card front">
    <div class="identity">
      <p class="name">Dana Velmonte</p>
      <p class="role">Principal</p>
    </div>

    <address class="address">
      480 Harbor View Road<br>
      Westbridge, 204718.
    </address>

    <ul class="contact-list">
      <li>
        <svg viewBox="0 0 24 24" aria-hidden="true"><path d="M6.6 10.8a15.1 15.1 0 0 0 6.6 6.6l2.2-2.2a1 1 0 0 1 1-.25 11.4 11.4 0 0 0 3.6.57 1 1 0 0 1 1 1V20a1 1 0 0 1-1 1A17 17 0 0 1 3 4a1 1 0 0 1 1-1h3.5a1 1 0 0 1 1 1c0 1.25.2 2.45.57 3.6a1 1 0 0 1-.25 1z"/></svg>
        044-310 582 946
      </li>
      <li>
        <svg viewBox="0 0 24 24" aria-hidden="true"><path d="M2 5h20v14H2z M2 5l10 8 10-8" fill="none" stroke="#f2f3f8" stroke-width="2.4"/></svg>
        hello@bktconsult.com
      </li>
      <li>
        <svg viewBox="0 0 24 24" aria-hidden="true"><circle cx="12" cy="12" r="10"/><path d="M2 12h20M12 2c3 3 3 17 0 20M12 2c-3 3-3 17 0 20" fill="none" stroke="#0c1452" stroke-width="1.6"/></svg>
        www.bktconsult.com
      </li>
    </ul>

    <div class="brand-band">
      <span class="brand-name">BKT Consulting</span>
    </div>
  </section>

  <section class="card card-back" aria-label="Business card back">
    <span class="brand-name">BKT Consulting</span>
  </section>

</main>
</body>
</html>
```